Need Cool Athletic Ticket Design for Students to use to enter a High School Athletic Sports Contest

I am needing a Event Ticket design for the Tarvendale High School Athletics department (https://bhs.tarvendaleps.com/). This will be a general admission ticket for ALL SPORTS. It will not be sport specific. The ticket will be 5.5" X 2" with serial numbering and perforation. It will also be a front and back ticket with the Tarvendale Athletics ticket design on one side and a Quillbrook Insurance Sponsorship ad design on the back. I have attached some ticket examples. The right side of the perforation must include space for the customer to fill out name, address, phone and email. It must include the ticket serial number on both portions, on the front side, of the ticket.

Requirements
Must have
• 5.5" X 2" ticket must have serial numbering and perforation. It must contain General Admission Ticket on the Tarvendale HS Side and a Quillbrook Ad (Boris Lindqvist Agency) on the back side of the ticket.
• The Quillbrook side of the Ticket will look similar to the business card (attached file) but please REMOVE the Direct phone (555-604-2718) and the email address (blindq@quillbrookpro.example). In place of the email address please add the agency's web address: www.quillbrookpro.example/blindq
• TAG LINE (at the bottom of the Quillbrook AD): Take the BORIS LINDQVIST CHALLENGE: If I can't save you money on your Auto Insurance; I'll buy you Dinner!
Nice to have
• Cool background graphics with the Tarvendale HS Logo on the top of the background.
Should not have
• Must NOT be sport specific.

```html
<!DOCTYPE html>
<html lang="en">
<head>
<meta charset="utf-8">
<title>Tarvendale High School – General Admission Ticket</title>
<link rel="stylesheet" href="https://fonts.googleapis.com/css2?family=Anton&family=Libre+Baskerville:wght@400;700&family=Roboto+Condensed:wght@400&display=swap">
<style>
  :root {
    --page: #dcdcde;
    --ticket-dark: #2a292b;
    --ticket-dark-2: #3a393b;
    --varsity-red: #d8232a;
    --deep-red: #6e0b0f;
    --silver: #a9abad;
    --silver-light: #d6d7d8;
    --white: #ffffff;
    --ink: #1b1b1b;
    --rule: #8a8a8a;
    --back-dark: #1f1f1f;
    --back-mid: #3a3a3a;
  }
  * { box-sizing: border-box; margin: 0; padding: 0; }
  html, body { width: 1200px; height: 1200px; overflow: hidden; background: var(--page); }
  .canvas { position: relative; width: 1200px; height: 1200px; }

  /* ---------- front: admission ticket ---------- */
  .ticket-front {
    position: absolute; left: 89px; top: 124px; width: 955px; height: 346px;
    overflow: hidden; box-shadow: 6px 8px 14px rgba(0,0,0,.35);
  }
  .front-backdrop {
    position: absolute; inset: 0;
    background: radial-gradient(ellipse at 60% 40%, var(--ticket-dark-2), var(--ticket-dark) 70%);
  }
  .front-chevron { position: absolute; left: 0; top: 0; width: 140px; height: 346px; }
  .school-title {
    position: absolute; left: 150px; top: 0; width: 480px; height: 180px;
    font-family: "Anton", sans-serif; font-weight: 400; color: var(--white);
    -webkit-text-stroke: 2px #000; paint-order: stroke fill;
    text-shadow: 3px 3px 0 #000;
    line-height: 1; text-align: center;
  }
  .school-title span { position: absolute; left: 0; width: 100%; display: block; white-space: nowrap; }
  .school-title .name { top: 22px; font-size: 76px; letter-spacing: 3px; }
  .school-title .level { top: 110px; font-size: 64px; letter-spacing: 3px; }
  .admission-line {
    position: absolute; left: 124px; top: 190px; width: 530px; white-space: nowrap;
    font-family: "Libre Baskerville", serif; font-weight: 700; font-size: 19px;
    color: #d9d9d9; font-variant: small-caps; letter-spacing: 0.3px; line-height: 34px;
  }
  .admission-line .accent { color: var(--varsity-red); font-size: 27px; font-variant: normal; }
  .mascot-name {
    position: absolute; display: flex; align-items: center; gap: 6px; white-space: nowrap;
    font-family: "Libre Baskerville", serif; font-weight: 700; color: var(--white);
  }
  .mascot-name .dot { width: 12px; height: 12px; border-radius: 50%; background: var(--varsity-red); flex: none; }
  .mascot-main { left: 128px; top: 289px; font-size: 15px; letter-spacing: 1px; }
  .mascot-stub { left: 674px; top: 298px; font-size: 11px; letter-spacing: 0; }
  .serial-pill { position: absolute; height: 24px; background: var(--white); border-radius: 12px; }
  .serial-main { left: 483px; top: 280px; width: 162px; }
  .serial-stub { left: 793px; top: 294px; width: 153px; }
  .perforation { position: absolute; left: 663px; top: 0; height: 346px; border-left: 1.5px dashed #9a9a9a; }
  .stub-form { position: absolute; left: 664px; top: 0; width: 291px; height: 256px; }
  .form-fields {
    position: absolute; left: 692px; top: 36px; width: 240px;
    font-family: "Roboto Condensed", sans-serif; font-size: 15px; color: var(--ink);
  }
  .field { position: absolute; left: 0; width: 100%; display: flex; align-items: flex-end; gap: 6px; height: 18px; }
  .field .line { flex: 1; border-bottom: 1px solid var(--ink); height: 100%; }

  /* ---------- back: sponsor ad ---------- */
  .ticket-back {
    position: absolute; left: 118px; top: 544px; width: 948px; height: 344px;
    overflow: hidden; box-shadow: 6px 8px 14px rgba(0,0,0,.35);
    background: radial-gradient(ellipse at 65% 30%, var(--back-mid), var(--back-dark) 75%);
  }
  .agent-photo { position: absolute; left: 0; top: 0; width: 260px; height: 344px; }
  .ad-copy {
    position: absolute; left: 262px; width: 670px; text-align: center;
    font-family: "Libre Baskerville", serif; font-weight: 700; color: var(--white);
  }
  .ad-headline { top: 28px; font-size: 24px; letter-spacing: 0.5px; white-space: nowrap; }
  .ad-promise { top: 70px; font-size: 22px; line-height: 38px; letter-spacing: 0.5px; }
  .ad-closer { top: 145px; font-size: 27px; letter-spacing: 0.5px; }
  .ad-rule { position: absolute; left: 266px; top: 202px; width: 660px; height: 2px; background: var(--rule); }
  .ad-contact { top: 220px; font-size: 21px; line-height: 35px; letter-spacing: 0.5px; }
  .ad-contact .web { font-size: 19px; }
</style>
</head>
<body>
<main class="canvas">

  <section class="ticket-front" aria-label="Tarvendale High School general admission ticket, front">
    <div class="front-backdrop" role="img" aria-label="Dark textured background with faint sports equipment graphics"></div>

    <svg class="front-chevron" viewBox="0 0 140 346" aria-hidden="true">
      <polygon points="0,0 28,0 82,173 28,346 0,346" fill="var(--deep-red)"/>
      <polygon points="28,0 70,0 124,173 70,346 28,346 82,173" fill="var(--silver)"/>
      <polygon points="28,0 44,0 98,173 44,346 28,346 82,173" fill="var(--silver-light)" opacity=".5"/>
    </svg>

    <h1 class="school-title">
      <span class="name">TARVENDALE</span>
      <span class="level">HIGH SCHOOL</span>
    </h1>
    <p class="admission-line">Admission <span class="accent">OPNE</span> for <span class="accent">ALL SPORTS</span></p>

    <div class="mascot-name mascot-main"><span class="dot"></span>RIDGEBACKS</div>
    <div class="serial-pill serial-main" aria-label="Serial number"></div>

    <div class="perforation"></div>

    <svg class="stub-form" viewBox="0 0 291 256" aria-hidden="true">
      <polygon points="0,230 147,256 291,230 291,212 147,240 0,212" fill="#8c8c8c"/>
      <polygon points="0,0 291,0 291,212 147,240 0,212" fill="var(--white)"/>
    </svg>
    <div class="form-fields">
      <div class="field" style="top:0">Name :<span class="line"></span></div>
      <div class="field" style="top:28px"><span class="line"></span></div>
      <div class="field" style="top:57px">Address :<span class="line"></span></div>
      <div class="field" style="top:84px"><span class="line"></span></div>
      <div class="field" style="top:107px">Phone :<span class="line"></span></div>
      <div class="field" style="top:133px">Email :<span class="line"></span></div>
    </div>

    <div class="mascot-name mascot-stub"><span class="dot"></span>RIDGEBACKS</div>
    <div class="serial-pill serial-stub" aria-label="Stub serial number"></div>
  </section>

  <section class="ticket-back" aria-label="Quillbrook Insurance sponsor ad, back">
    <svg class="agent-photo" viewBox="0 0 260 344" role="img" aria-label="Portrait photo of agent Boris Lindqvist in a dark suit">
      <defs>
        <linearGradient id="portraitTone" x1="0" y1="0" x2="1" y2="1">
          <stop offset="0" stop-color="#7a6360"/>
          <stop offset=".55" stop-color="#5d5a66"/>
          <stop offset="1" stop-color="#2a2d3a"/>
        </linearGradient>
      </defs>
      <path d="M0,0 H246 L238,22 L248,48 L240,80 L250,112 L242,150 L252,190 L244,230 L254,270 L246,310 L252,344 H0 Z" fill="url(#portraitTone)"/>
      <path d="M246,0 L238,22 L248,48 L240,80 L250,112 L242,150 L252,190 L244,230 L254,270 L246,310 L252,344" fill="none" stroke="#f2f2f2" stroke-width="2"/>
    </svg>

    <p class="ad-copy ad-headline">TAKE THE BORIS LINDQVIST CHALLENGE:</p>
    <p class="ad-copy ad-promise">If I can't save you money on<br>your Auto Insurance;</p>
    <p class="ad-copy ad-closer">I'LL BUY YOU DINNER!</p>
    <div class="ad-rule"></div>
    <p class="ad-copy ad-contact">
      482 W 9th Street Tarvendale, OK 74990<br>
      Office : 555 210 4473 Fax : 555 210 4486<br>
      <span class="web">www.quillbrookpro.example/blindq</span>
    </p>
  </section>

</main>
</body>
</html>
```